Take-away menu design

We need a double-sided menu brochure designed, the measurements are 195mmx280mm. We have all the details provided for you such as color RGB, content, fonts, logo and the precedent. We would like our content to be implemented into the precedent menu provided.

Fish and Chips

• Museo Slab 300, Kauvita Greek Bold Regular

```html
<!DOCTYPE html>
<html lang="en">
<head>
<meta charset="utf-8">
<title>The Cod Cove – Fish and Chips Menu</title>
<link rel="stylesheet" href="https://fonts.googleapis.com/css2?family=Roboto+Slab:wght@300;400;800&family=Barlow+Semi+Condensed:wght@600&display=swap">
<style>
  :root {
    --ink: #231f20;
    --blue: #0a94f0;
    --paper: #ffffff;
    --text: #231f20;
  }
  * { box-sizing: border-box; margin: 0; padding: 0; }
  html, body { width: 836px; height: 1200px; overflow: hidden; background: var(--paper); }
  body { font-family: "Roboto Slab", Georgia, serif; font-weight: 300; color: var(--text); font-size: 12.4px; }
  .menu { position: relative; width: 836px; height: 1200px; }

  .masthead { position: absolute; left: 0; top: 0; width: 836px; height: 107px; background: var(--ink); }
  .brand-mark { position: absolute; left: 290px; top: 38px; width: 30px; height: 30px; border-radius: 50%; background: var(--blue); }
  .brand-name { position: absolute; left: 356px; top: 40px; font-weight: 300; font-size: 21px; letter-spacing: 1.6px; color: var(--paper); white-space: nowrap; }
  .brand-tagline { position: absolute; left: 410px; top: 66px; font-family: "Barlow Semi Condensed", Arial, sans-serif; font-weight: 600; font-size: 12px; letter-spacing: 0.6px; color: var(--blue); }

  .block { position: absolute; width: 371px; }
  .col-left { left: 30px; }
  .col-right { left: 435px; }

  .section-bar { position: absolute; height: 31px; width: 371px; background: var(--ink); color: var(--paper);
    font-family: "Barlow Semi Condensed", Arial, sans-serif; font-weight: 600; font-size: 16.5px;
    padding-left: 8px; line-height: 32px; letter-spacing: 0.3px; }
  .section-bar .plus { color: var(--blue); }

  .note { position: absolute; width: 371px; line-height: 16px; }

  .menu-list { position: absolute; width: 371px; list-style: none; }
  .menu-list li { position: relative; height: 33.2px; border-top: 3px solid var(--ink);
    display: flex; align-items: center; white-space: nowrap; }
  .menu-list.closed li:last-child { border-bottom: 3px solid var(--ink); height: 36.2px; }
  .item-name { color: var(--blue); font-weight: 800; }
  .item-name.dark { color: var(--ink); }
  .price { position: absolute; right: 0; top: 50%; transform: translateY(-50%); width: 16px; height: 16px;
    background: var(--blue); color: var(--paper); font-weight: 800; font-size: 10.5px;
    text-align: center; line-height: 16px; }

  .described li { height: auto; display: block; padding: 5px 0 8px; line-height: 15.4px; white-space: normal; }
  .described .price { top: 9px; transform: none; }
  .described .desc { padding-right: 26px; }

  .prep { position: absolute; left: 30px; top: 531px; width: 371px; height: 24px; }
  .prep-label { position: absolute; left: 0; top: 4px; }
  .prep-select { position: absolute; left: 122px; top: 0; width: 179px; height: 24px; border: 1px solid var(--ink);
    padding-left: 11px; line-height: 22px; }
  .prep-select svg { position: absolute; right: 11px; top: 9px; }
  .prep-options { position: absolute; left: 97px; top: 560px; display: flex; gap: 10px; font-size: 10px; text-transform: uppercase; }
  .prep-options span::before { content: ""; display: inline-block; width: 9px; height: 9px; border: 1px solid var(--ink);
    margin-right: 4px; vertical-align: -1px; }
</style>
</head>
<body>
<main class="menu">
  <header class="masthead">
    <span class="brand-mark"></span>
    <h1 class="brand-name">THE COD COVE</h1>
    <p class="brand-tagline">FISH AND CHIPS</p>
  </header>

  <!-- Fish + Chips -->
  <h2 class="section-bar col-left" style="top:121px">FISH <span class="plus">+</span> CHIPS</h2>
  <p class="note col-left" style="left:29px;top:160px">[Served with your choice of chips, tartare sauce &amp; lemon.]</p>
  <ul class="menu-list closed col-left" style="left:30px;top:184px">
    <li><span><span class="item-name">Cod</span> &amp; chips (NZ, wild caught)</span><span class="price">15</span></li>
    <li><span><span class="item-name">Whiting</span> &amp; chips (QLD, wild caught, crumbed only)</span><span class="price">17</span></li>
    <li><span><span class="item-name">Flathead</span> &amp; chips (SA, wild caught, beer battered only)</span><span class="price">20</span></li>
    <li><span><span class="item-name">Snapper</span> &amp; chips (NT, wild caught)</span><span class="price">20</span></li>
    <li><span><span class="item-name">Barramundi</span> &amp; chips (NT, ocean farmed)</span><span class="price">20</span></li>
    <li><span><span class="item-name">Salmon</span> &amp; chips (TAS, ocean farmed)</span><span class="price">21</span></li>
    <li><span><span class="item-name">Crumbed Calamari</span> (8) &amp; chips</span><span class="price">15</span></li>
    <li><span><span class="item-name">Salt &amp; Pepper Calamari</span> (8) &amp; chips</span><span class="price">17</span></li>
    <li><span><span class="item-name">Crumbed Prawns</span> (5) &amp; chips</span><span class="price">28</span></li>
    <li><span><span class="item-name">BBQ Prawn Skewers</span> (5) &amp; chips</span><span class="price">28</span></li>
  </ul>

  <div class="prep">
    <span class="prep-label">Made fresh to order</span>
    <span class="prep-select">Choose your preparation
      <svg width="7" height="5" viewBox="0 0 7 5"><path d="M0 0H7L3.5 5Z" fill="#0a94f0"/></svg>
    </span>
  </div>
  <div class="prep-options"><span>Grilled</span><span>Crumbed</span><span>Beer Battered</span></div>

  <!-- Platters -->
  <h2 class="section-bar col-left" style="top:584px">COOKED SEAFOOD PLATTERS</h2>
  <p class="note col-left" style="left:29px;top:620px;line-height:15.4px">Cooked Seafood Platters include: whiting, calamari, salt &amp;<br>pepper calamari, prawns, sea scallops, chips,<br>one of our freshly made salads, tartare sauce &amp; lemon.</p>
  <ul class="menu-list col-left" style="left:30px;top:677px">
    <li><span class="item-name dark">Cooked Platter for One</span><span class="price">26</span></li>
    <li><span class="item-name dark">Cooked Platter for Two</span><span class="price">51</span></li>
    <li><span class="item-name dark">Cooked Platter for Three</span><span class="price">76</span></li>
  </ul>
  <p class="note col-left" style="left:30px;top:776px">Our seafood platters are available crumbed only.</p>

  <!-- Starters -->
  <h2 class="section-bar col-left" style="top:808px">STARTERS <span class="plus">+</span> SIDES</h2>
  <ul class="menu-list col-left" style="left:30px;top:855px">
    <li>Crumbed Calamari (8)<span class="price">10</span></li>
    <li>Salt &amp; Pepper Calamari (8)<span class="price">12</span></li>
    <li>Crumbed Sea Scallop<span class="price">5</span></li>
    <li>Crumbed Prawn<span class="price">5</span></li>
    <li>BBQ Prawn Skewer<span class="price">5</span></li>
    <li>Onion Rings (8)<span class="price">10</span></li>
    <li>Popcorn Chicken<span class="price">10</span></li>
    <li>Potato Scallop<span class="price">4</span></li>
    <li>Grilled Halloumi (3 slices)<span class="price">12</span></li>
    <li>Fried Halloumi (3 slices, crumbed)<span class="price">12</span></li>
  </ul>

  <!-- Salads -->
  <h2 class="section-bar col-right" style="top:121px">SALADS</h2>
  <p class="note col-right" style="left:434px;top:160px">[Freshly prepared to order using local produce.]</p>
  <ul class="menu-list described col-right" style="left:435px;top:184px">
    <li><span class="item-name">Greek</span><span class="price">10</span><p class="desc">Lettuce, cucumber, tomato, red onion, Kalamata olives, feta, Greek peppers, wild oregano, dressed in Greek extra virgin olive Oil vinaigrette.</p></li>
    <li><span class="item-name">Roast Pumpkin</span><span class="price">10</span><p class="desc">Roast pumpkin, wild rocket, Parmigiano Reggiano, toasted pine nuts, dressed in Greek extra virgin olive oil &amp; vintage balsamic vinegar.</p></li>
    <li><span class="item-name">Slaw</span><span class="price">10</span><p class="desc">Shredded red &amp; green cabbage, carrot, tossed in a light mayonnaise dressing.</p></li>
    <li><span class="item-name">Asian Slaw</span><span class="price">10</span><p class="desc">Shredded red &amp; green cabbage, carrot, spring onion, crispy noodles, sesame seeds, tossed in a sweet soy dressing.</p></li>
  </ul>

  <!-- Burgers -->
  <h2 class="section-bar col-right" style="top:488px">BURGERS <span class="plus">+</span> TACOS</h2>
  <ul class="menu-list described col-right" style="left:435px;top:531px">
    <li><span class="item-name">Fish Burger</span> &amp; chips<span class="price">16</span><p class="desc">Crumbed cod fillet, shredded lettuce, tomato &amp; tartare sauce in a toasted bun.</p></li>
    <li><span class="item-name">Fish Tacos</span> (3) &amp; chips<span class="price">18</span><p class="desc">Beer battered cod, shredded red &amp; green cabbage, carrot, chipotle mayonnaise in soft flour tortillas.</p></li>
    <li><span class="item-name">Chicken Burger</span> &amp; chips<span class="price">16</span><p class="desc">Grilled free range chicken tenders, shredded lettuce, tomato, cheese, avocado, aioli in a toasted bun.</p></li>
    <li><span class="item-name">Steak Burger</span> &amp; chips<span class="price">18</span><p class="desc">Grilled grass fed rib fillet, shredded lettuce, tomato, cheese, caramelised onion, BBQ sauce in a toasted bun.</p></li>
  </ul>

  <!-- Chips -->
  <h2 class="section-bar col-right" style="top:788px">CHIPS</h2>
  <ul class="menu-list col-right" style="left:435px;top:832px">
    <li>Chips GF<span class="price">6</span></li>
    <li>Beer Battered Chips<span class="price">8</span></li>
    <li>Sweet Potato Chips<span class="price">8</span></li>
  </ul>

  <!-- Sauces -->
  <h2 class="section-bar col-right" style="top:940px">SAUCES</h2>
  <ul class="menu-list col-right" style="left:435px;top:983px">
    <li>Tartare, Aioli, Tomato &amp; Chipotle Mayonnaise<span class="price">2</span></li>
  </ul>

  <!-- Children's -->
  <h2 class="section-bar col-right" style="top:1024px">CHILDREN'S FISH <span class="plus">+</span> CHIPS</h2>
  <ul class="menu-list col-right" style="left:435px;top:1068px">
    <li><span><span class="item-name">Fish Fingers</span> (4) &amp; chips</span><span class="price">12</span></li>
    <li><span><span class="item-name">Crumbed Calamari</span> (4) &amp; chips</span><span class="price">12</span></li>
    <li><span><span class="item-name">Popcorn Chicken</span> &amp; chips</span><span class="price">12</span></li>
  </ul>
</main>
</body>
</html>
```